Flyer design for the Harvest Lantern Summit 2019 (HALSUM)

Design a flyer for our annual conference with basic information about the conference: conference logo and year, Conference name: Harvest Lantern Summit Location: Talbot Community Center (Downtown Portland)482 Wexley Street, Portland, ME 04109, Date: August 8th, 9th, 10th and 11th, 2019Start time 7:00PMI would like the following three words added to the flyer. These words describe the vision of the conference: Prophetic, Fire, Overflow,

Contact info:
Website: www.vostel.org
Phone: 207 555 3184
Email: contact@meadowcrest.org

Target Market(s)

Young adults living in the United States

Industry/Entity Type

Religious

Font styles to use
Sans Serif

Colors

Designer to choose colors to be used in the design.

Requirements
Must have
• HALSUM must logo standout, the reader should be able to take a quick look and find key info,
Should not have
• Cross image, church image

```html
<!DOCTYPE html>
<html lang="en">
<head>
<meta charset="utf-8">
<title>Harvest Lantern Summit 2019 – Flyer</title>
<link rel="stylesheet" href="https://fonts.googleapis.com/css2?family=Montserrat:wght@500;600;700;800&family=Oswald:wght@700&display=swap">
<style>
  :root {
    --page-bg: #6b6b6b;
    --paper: #ffffff;
    --brand-blue: #1466b3;
    --blue-light: #0b72c4;
    --blue-deep: #08498c;
    --brand-orange: #f28c12;
    --fire-red: #c7300c;
    --fire-dark: #3a0804;
    --ink: #1c1c1c;
  }
  html, body {
    margin: 0;
    width: 1200px;
    height: 1200px;
    overflow: hidden;
    background: var(--page-bg);
  }
  .flyer {
    position: absolute;
    left: 201px;
    top: 40px;
    width: 798px;
    height: 1120px;
    box-shadow: 0 6px 18px rgba(0,0,0,.35);
  }
  .flyer svg { display: block; width: 100%; height: 100%; }
  .brand-name { font-family: "Montserrat", sans-serif; font-weight: 800; fill: var(--brand-blue); }
  .brand-year { font-family: "Montserrat", sans-serif; font-weight: 700; fill: var(--brand-orange); }
  .headline-top { font-family: "Oswald", sans-serif; font-weight: 700; fill: var(--brand-orange); }
  .headline-bottom { font-family: "Montserrat", sans-serif; font-weight: 800; fill: #fff; }
  .vision { font-family: "Montserrat", sans-serif; font-weight: 800; fill: #fff; }
  .event-info { font-family: "Montserrat", sans-serif; font-weight: 700; fill: #fff; }
  .venue { font-family: "Montserrat", sans-serif; font-weight: 500; fill: #fff; }
  .contact-label { font-family: "Montserrat", sans-serif; font-weight: 600; fill: #fff; }
  .contact-phone { font-family: "Montserrat", sans-serif; font-weight: 800; fill: var(--ink); }
  .contact-text { font-family: "Montserrat", sans-serif; font-weight: 500; fill: var(--ink); }
  .icon-stroke { fill: none; stroke: var(--brand-orange); stroke-width: 2; }
  .icon-fill { fill: var(--brand-orange); }
</style>
</head>
<body>
<div class="flyer">
  <svg viewBox="0 0 751 1054" xmlns="http://www.w3.org/2000/svg">
    <defs>
      <radialGradient id="fireGlow" cx="0.55" cy="0.45" r="0.7">
        <stop offset="0" stop-color="#f7a23a"/>
        <stop offset="0.45" stop-color="#e3561a"/>
        <stop offset="0.8" stop-color="var(--fire-red)"/>
        <stop offset="1" stop-color="var(--fire-dark)"/>
      </radialGradient>
      <radialGradient id="blueField" cx="0.5" cy="0.45" r="0.7">
        <stop offset="0" stop-color="var(--blue-light)"/>
        <stop offset="1" stop-color="var(--blue-deep)"/>
      </radialGradient>
    </defs>

    <rect class="paper" width="751" height="1054" fill="var(--paper)"/>

    <!-- Conference mark -->
    <g class="brand">
      <text class="brand-name" x="25" y="88" font-size="66" textLength="310" lengthAdjust="spacingAndGlyphs">HALSUM</text>
      <line x1="25" y1="112" x2="100" y2="112" stroke="var(--brand-orange)" stroke-width="2"/>
      <text class="brand-year" x="168" y="122" font-size="30" text-anchor="middle" letter-spacing="14">2019</text>
      <line x1="258" y1="112" x2="334" y2="112" stroke="var(--brand-orange)" stroke-width="2"/>
    </g>

    <!-- Hero image area -->
    <path class="hero-image" role="img" aria-label="Vintage studio microphone engulfed in bright flames"
      d="M0,275 C150,170 360,95 751,85 L751,565 C620,495 500,470 375,470 C250,470 120,490 0,525 Z"
      fill="url(#fireGlow)"/>

    <!-- Blue information field -->
    <path class="info-field" d="M0,525 C120,490 250,470 375,470 C500,470 620,495 751,565 L751,978 L0,978 Z" fill="url(#blueField)"/>

    <text class="headline-top" x="378" y="604" font-size="88" text-anchor="middle" textLength="590" lengthAdjust="spacingAndGlyphs">HARVEST LANTERN</text>
    <text class="headline-bottom" x="376" y="667" font-size="64" text-anchor="middle" letter-spacing="2">SUMMIT</text>

    <rect class="vision-band" x="0" y="680" width="751" height="46" fill="var(--brand-orange)"/>
    <text class="vision" x="375" y="713" font-size="26" text-anchor="middle">PROPHETIC, FIRE, OVERFLOW.</text>

    <!-- Calendar icon -->
    <g class="icon-calendar">
      <rect class="icon-stroke" x="357" y="742" width="32" height="28" rx="3"/>
      <line x1="357" y1="751" x2="389" y2="751" stroke="var(--brand-orange)" stroke-width="3"/>
      <line x1="364" y1="738" x2="364" y2="745" stroke="var(--brand-orange)" stroke-width="2"/>
      <line x1="382" y1="738" x2="382" y2="745" stroke="var(--brand-orange)" stroke-width="2"/>
      <rect class="icon-fill" x="362" y="756" width="5" height="4"/>
      <rect class="icon-fill" x="370" y="756" width="5" height="4"/>
      <rect class="icon-fill" x="362" y="763" width="5" height="4"/>
      <circle cx="388" cy="768" r="7" fill="var(--blue-light)" stroke="var(--brand-orange)" stroke-width="2"/>
      <path d="M388,764 V768 H391" fill="none" stroke="var(--brand-orange)" stroke-width="1.5"/>
    </g>

    <text class="event-info" x="376" y="806" font-size="26" text-anchor="middle">August 8th, 9th, 10th and 11th,2019</text>
    <text class="event-info" x="376" y="840" font-size="26" text-anchor="middle">Start time 7:00PM</text>

    <!-- Location pin -->
    <path class="icon-fill" d="M377,862 c-6,0 -10,4.5 -10,10 c0,7 10,16 10,16 s10,-9 10,-16 c0,-5.5 -4,-10 -10,-10 z M377,868 a4,4 0 1 1 0,8 a4,4 0 1 1 0,-8 z" fill-rule="evenodd"/>

    <text class="venue" x="376" y="912" font-size="20" text-anchor="middle">Talbot Community Center (Downtown Portland)</text>
    <text class="venue" x="376" y="937" font-size="20" text-anchor="middle">482 Wexley Street, Portland, ME 04109</text>

    <!-- Contact strip -->
    <rect x="0" y="977" width="751" height="2" fill="var(--brand-orange)"/>
    <rect class="contact-pill" x="273" y="960" width="206" height="38" rx="19" fill="var(--brand-orange)"/>
    <text class="contact-label" x="376" y="987" font-size="24" text-anchor="middle">Contact info:</text>

    <g class="contact-phone-item">
      <path class="icon-fill" d="M27,1010 l5,-2 l4,7 l-3,3 c1.5,3 4,5.5 7,7 l3,-3 l7,4 l-2,5 c-11,0 -21,-10 -21,-21 z"/>
      <text class="contact-phone" x="51" y="1026" font-size="20">207 555 3184</text>
    </g>

    <g class="contact-email-item">
      <rect class="icon-fill" x="253" y="1013" width="14" height="10" rx="1"/>
      <path d="M253,1014 L260,1019 L267,1014" fill="none" stroke="#fff" stroke-width="1.2"/>
      <text class="contact-text" x="276" y="1024" font-size="19">contact@meadowcrest.org</text>
    </g>

    <g class="contact-web-item">
      <circle class="icon-stroke" cx="572" cy="1020" r="7.5" stroke-width="1.6"/>
      <ellipse class="icon-stroke" cx="572" cy="1020" rx="3.2" ry="7.5" stroke-width="1.3"/>
      <line x1="564.5" y1="1020" x2="579.5" y2="1020" stroke="var(--brand-orange)" stroke-width="1.3"/>
      <text class="contact-text" x="588" y="1026" font-size="19">www.vostel.org</text>
    </g>
  </svg>
</div>
</body>
</html>
```